ROLL UP CREATION

For a trade show we need three visuals to be seen see pdf file with slogans and photos. I expect from you a nice and attractive formatting that is urgent. the files must be in high definition for the printer. You will find enclosed the 3 visuals, photos the basic logo by adding the .com and the photo of the Rollup For a trade show we need to see the pdf file with slogans and photos. I expect from you a nice and attractive formatting that is urgent. the files must be in high definition for the printer. For a trade show we need to see the pdf file with slogans and photos. I expect from you a nice and attractive formatting that is urgent. the files must be in high definition for the printer. For a trade show we need to see the pdf file with slogans and photos. I expect from you a nice and attractive formatting that is urgent. the files must be in high definition for the printer. For a trade show we need to see the pdf file with slogans and photos. I expect from you a nice and attractive formatting that is urgent. the files must be in high definition for the printer. For a trade show we need to see the pdf file with slogans and photos. I expect from you a nice and attractive formatting that is urgent. the files must be in high definition for the printer. For a trade show we need to see the pdf file with slogans and photos. I expect from you a nice and attractive formatting that is urgent. the files must be in high definition for the printer. For a trade show we need to see the pdf file with slogans and photos. I expect from you a nice and attractive formatting that is urgent. the files must be in high definition for the printer. For a trade show we need to see the pdf file with slogans and photos. I expect from you a nice and attractive formatting that is urgent. the files must be in high definition for the printer. For a trade show we need to see the pdf file with slogans and photos. I expect from you a nice and attractive formatting that is urgent. the files must be in high definition for the printer.

Target Market(s)

Professional

Industry/Entity Type

Trade

Requirements
Must have
• the project the messages and the photos are chosen all the way to a nice and professional result. This is urgently the size of the rollup is 200/85.
Nice to have
• the bottom of the rollup on 40 cm must be just color because in an exhibition the visitors can not see the messages near the ground.
Should not have
• no green color

```html
<!DOCTYPE html>
<html lang="fr">
<head>
<meta charset="utf-8">
<title>Vestalo – Roll-up</title>
<link rel="stylesheet" href="https://fonts.googleapis.com/css2?family=Quicksand:wght@500;600&display=swap">
<style>
  :root {
    --page: #ffffff;
    --shadow: #b3b3b3;
    --blue-top: #3573b3;
    --blue-mid: #4e6ea9;
    --purple-bottom: #7b5088;
    --ring-blue: #1d6fb8;
    --white: #ffffff;
    --photo-light: #eef1f3;
    --photo-mid: #cfd8de;
  }
  html, body {
    margin: 0;
    padding: 0;
    width: 1200px;
    height: 1000px;
    overflow: hidden;
    background: var(--page);
    font-family: "Quicksand", sans-serif;
  }
  .canvas {
    position: relative;
    width: 1200px;
    height: 1000px;
  }
  .rollup-shadow {
    position: absolute;
    left: 405px;
    top: 30px;
    width: 410px;
    height: 948px;
    background: var(--shadow);
  }
  .rollup {
    position: absolute;
    left: 397px;
    top: 22px;
    width: 410px;
    height: 948px;
    overflow: hidden;
    background: var(--white);
  }
  .rollup-art {
    position: absolute;
    inset: 0;
    display: block;
  }
  .brand {
    position: absolute;
    left: 30px;
    top: 44px;
    display: flex;
    align-items: center;
    gap: 38px;
    color: var(--white);
  }
  .brand-dot {
    width: 44px;
    height: 44px;
    border-radius: 50%;
    background: var(--white);
  }
  .brand-name {
    font-weight: 500;
    font-size: 42px;
    letter-spacing: 0.5px;
    line-height: 1;
  }
  .slogan {
    position: absolute;
    left: 27px;
    margin: 0;
    color: var(--white);
    font-weight: 600;
    font-size: 20.5px;
    line-height: 30px;
    letter-spacing: 0.3px;
    white-space: nowrap;
  }
  .slogan-top { top: 155px; }
  .slogan-bottom { top: 684px; }
</style>
</head>
<body>
<div class="canvas">
  <div class="rollup-shadow"></div>
  <section class="rollup">
    <svg class="rollup-art" width="410" height="948" viewBox="0 0 410 948">
      <defs>
        <linearGradient id="backdrop" x1="0" y1="0" x2="0" y2="1">
          <stop offset="0" stop-color="var(--blue-top)"/>
          <stop offset="0.35" stop-color="var(--blue-mid)"/>
          <stop offset="0.75" stop-color="var(--purple-bottom)"/>
          <stop offset="1" stop-color="var(--purple-bottom)"/>
        </linearGradient>
        <linearGradient id="photo" x1="0" y1="0" x2="0" y2="1">
          <stop offset="0" stop-color="var(--photo-light)"/>
          <stop offset="0.5" stop-color="var(--photo-mid)"/>
          <stop offset="1" stop-color="var(--photo-light)"/>
        </linearGradient>
      </defs>
      <rect width="410" height="948" fill="url(#backdrop)" role="img" aria-label="Façade d'immeuble de bureaux vue en contre-plongée, teintée bleu et violet"/>
      <rect class="side-strip" x="363" y="0" width="47" height="449" fill="var(--white)"/>
      <circle class="frame-ring" cx="206" cy="449" r="210" fill="var(--white)"/>
      <circle class="photo-disc" cx="206" cy="449" r="155" fill="url(#photo)" stroke="var(--ring-blue)" stroke-width="4" role="img" aria-label="Photo d'une gestionnaire débordée derrière des piles de classeurs"/>
    </svg>

    <div class="brand">
      <span class="brand-dot"></span>
      <span class="brand-name">vestalo.com</span>
    </div>

    <p class="slogan slogan-top">Finis le stress pour la gestion de<br>vos copropriétés...</p>
    <p class="slogan slogan-bottom">VESTALO le portail dédié aux<br>professionnels de l´immobilier.</p>
  </section>
</div>
</body>
</html>
```